Quellbyte Business cards template

We're looking for something modern and elegant. We are a reseller of technology (computers, datacenter, etc). Color theme would be "only" white with the incorporation of the blue that's present on our website (Quellbyte.com) and logo file. We would like for the card to provide all the necessary info for the specific person (Phone#, fax#, email, name, website URL) . I'm attaching the logo file to this request. Please have it show Montreal/New York somewhere, without providing specific addresses.

Target Market(s)

All b2b

Industry/Entity Type

Business

Contact Information for Business Card

Please have the color scheme be represented by only the white and blue from our website (Quellbyte.com) and logo. We would like to logo on the card, but not big and overwhelming. This card will be used as a template for anybody within the company, it should display the user's name, phone#, fax#, email, job title and website URL. Please have it show Montreal/New York somewhere, without providing our specific addresses. Really, we're looking for a clean, simple and elegant look.

Font styles to use
Serif

Requirements
Must have
• Please see card details
Nice to have
• Please see card details
Should not have
• Anything tacky or tagline.

```html
<!DOCTYPE html>
<html lang="en">
<head>
<meta charset="utf-8">
<title>Quellbyte Business Cards</title>
<link href="https://fonts.googleapis.com/css2?family=Fira+Sans:wght@400;600&display=swap" rel="stylesheet">
<style>
  :root {
    --bg: #e9ebee;
    --white: #ffffff;
    --blue-deep: #0b5494;
    --blue-mid: #0d67a8;
    --blue-bright: #1774b8;
    --blue-light: #5b95d6;
    --ink: #1266b0;
  }
  html, body { margin: 0; padding: 0; width: 1200px; height: 873px; overflow: hidden; background: var(--bg); }
  .canvas { position: relative; width: 1200px; height: 873px; font-family: "Fira Sans", sans-serif; }
  .card { position: absolute; top: 288px; width: 520px; height: 297px; overflow: hidden; box-shadow: 0 10px 28px rgba(0,0,0,.18); }
  .card-front { left: 50px; background: var(--white); }
  .card-back { left: 630px; background: var(--blue-mid); }
  .card svg.bands { position: absolute; inset: 0; width: 100%; height: 100%; }
  .brand { position: absolute; font-weight: 600; letter-spacing: .5px; }
  .card-front .brand { left: 36px; top: 30px; font-size: 24px; color: var(--ink); }
  .card-back .brand { left: 0; right: 0; top: 128px; text-align: center; font-size: 38px; color: var(--white); }
  .person { position: absolute; left: 36px; top: 84px; color: var(--ink); }
  .person-name { font-size: 17px; font-weight: 600; letter-spacing: 5px; margin: 0; }
  .person-title { font-size: 9px; letter-spacing: 3px; margin: 4px 0 0; }
  .contacts { position: absolute; left: 36px; top: 142px; margin: 0; padding: 0; list-style: none; color: var(--ink); font-size: 10px; letter-spacing: 2.6px; }
  .contacts li { display: flex; align-items: center; gap: 9px; height: 19px; }
  .contacts svg { width: 11px; height: 11px; fill: var(--ink); flex: none; }
</style>
</head>
<body>
<div class="canvas">
  <section class="card card-front">
    <svg class="bands" viewBox="0 0 520 297" preserveAspectRatio="none">
      <polygon points="330,0 520,0 520,297 230,297" fill="var(--blue-mid)"/>
      <polygon points="395,0 470,0 380,297 300,297" fill="var(--blue-deep)"/>
      <polygon points="470,0 520,0 520,60 440,297 380,297" fill="var(--blue-bright)"/>
      <polygon points="500,160 520,120 520,297 470,297" fill="var(--blue-light)"/>
      <polygon points="0,230 0,297 90,297" fill="var(--blue-deep)"/>
      <polygon points="0,262 0,297 40,297" fill="var(--blue-light)"/>
    </svg>
    <div class="brand">Quellbyte</div>
    <div class="person">
      <p class="person-name">JOHN SMITH</p>
      <p class="person-title">JOB TITLE</p>
    </div>
    <ul class="contacts">
      <li><svg viewBox="0 0 12 12"><path d="M2 1h3l1 3-2 1a7 7 0 0 0 3 3l1-2 3 1v3c-6 0-9-3-9-9z"/></svg>15550142277</li>
      <li><svg viewBox="0 0 12 12"><rect x="2" y="1" width="8" height="4"/><rect x="1" y="5" width="10" height="6" rx="1"/></svg>15550142277</li>
      <li><svg viewBox="0 0 12 12"><path d="M1 2h10v8H1z M1 2l5 4 5-4" stroke="var(--white)" stroke-width=".8"/></svg>MAIL@QUELLBYTE.COM</li>
      <li><svg viewBox="0 0 12 12"><circle cx="6" cy="6" r="5"/><path d="M1 6h10M6 1v10" stroke="var(--white)" stroke-width=".8"/></svg>WWW.QUELLBYTE.COM</li>
      <li><svg viewBox="0 0 12 12"><path d="M6 11S2 7 2 4.5a4 4 0 0 1 8 0C10 7 6 11 6 11z"/><circle cx="6" cy="4.5" r="1.4" fill="var(--white)"/></svg>MONTREAL / NEW YORK</li>
    </ul>
  </section>

  <section class="card card-back">
    <svg class="bands" viewBox="0 0 520 297" preserveAspectRatio="none">
      <polygon points="0,0 60,0 0,160" fill="var(--blue-light)"/>
      <polygon points="60,0 170,0 80,297 0,297 0,160" fill="var(--blue-bright)"/>
      <polygon points="170,0 350,0 300,297 80,297" fill="var(--blue-deep)"/>
      <polygon points="350,0 430,0 380,297 300,297" fill="var(--blue-mid)"/>
      <polygon points="430,0 520,0 520,297 380,297" fill="var(--blue-bright)"/>
      <polygon points="520,180 520,297 470,297" fill="var(--blue-light)"/>
    </svg>
    <div class="brand">Quellbyte</div>
  </section>
</div>
</body>
</html>
```